Fireworks company

COLORFUL design, incorporating logo (attached).
Information to be included:
PO BOX 4829
Marlow Vale 3891
Ph 03 5461 8237
Fax 03 5387 9216
Email sales@brindarockets.com.au
Web www.brindarockets.com.au

Check out our website for more inspiration? :-)

```html
<!DOCTYPE html>
<html lang="en">
<head>
<meta charset="utf-8">
<title>Brinda Rockets Letterhead</title>
<link href="https://fonts.googleapis.com/css2?family=Source+Sans+3:wght@400;600;700&display=swap" rel="stylesheet">
<style>
  :root {
    --paper: #ffffff;
    --brand-orange: #ec5a24;
    --band-orange: #ef5323;
    --band-glow: #f7a21b;
    --wave-brown: #6a3713;
    --wave-yellow: #ece91f;
    --footer-text: #ffffff;
  }
  html, body {
    margin: 0;
    padding: 0;
    width: 970px;
    height: 1200px;
    overflow: hidden;
    background: var(--paper);
  }
  .letterhead {
    position: relative;
    width: 970px;
    height: 1200px;
    background: var(--paper);
    font-family: "Source Sans 3", "Myriad Pro", Arial, sans-serif;
  }
  .brand {
    position: absolute;
    top: 82px;
    left: 0;
    width: 970px;
    text-align: center;
    color: var(--brand-orange);
    font-weight: 700;
    text-transform: uppercase;
    line-height: 0.95;
  }
  .brand__line {
    display: block;
    font-size: 52px;
    letter-spacing: 2px;
  }
  .brand__line--large {
    font-size: 68px;
    letter-spacing: 1px;
  }
  .footer-waves {
    position: absolute;
    left: 0;
    top: 1000px;
    width: 970px;
    height: 200px;
    display: block;
  }
  .postal-address {
    position: absolute;
    left: 53px;
    top: 1157px;
    margin: 0;
    color: var(--footer-text);
    font-size: 16px;
    font-weight: 400;
    font-style: normal;
  }
  .contact-list {
    position: absolute;
    left: 653px;
    top: 1093px;
    margin: 0;
    padding: 0;
    list-style: none;
    color: var(--footer-text);
  }
  .contact-list__item {
    display: flex;
    align-items: center;
    height: 20px;
    font-size: 14.5px;
    font-weight: 400;
  }
  .contact-list__item--phone {
    height: 26px;
    font-size: 18.5px;
    font-weight: 700;
    letter-spacing: 0.5px;
  }
  .contact-list__icon {
    width: 14px;
    height: 14px;
    margin-right: 10px;
    flex: none;
    fill: var(--footer-text);
  }
</style>
</head>
<body>
<main class="letterhead">
  <header class="brand">
    <span class="brand__line">Brinda</span>
    <span class="brand__line brand__line--large">Rockets</span>
  </header>

  <svg class="footer-waves" viewBox="0 0 970 200" preserveAspectRatio="none" aria-hidden="true">
    <defs>
      <radialGradient id="bandGlow" cx="0.5" cy="0.75" r="0.55" gradientUnits="objectBoundingBox">
        <stop offset="0" stop-color="var(--band-glow)"/>
        <stop offset="1" stop-color="var(--band-orange)"/>
      </radialGradient>
    </defs>
    <path d="M0,124 C250,112 420,44 700,26 C820,18 905,20 970,26 L970,200 L0,200 Z" fill="var(--wave-brown)"/>
    <path d="M0,122 C200,108 390,64 546,36 L556,58 C410,86 230,124 0,138 Z" fill="var(--wave-yellow)"/>
    <path d="M0,134 C300,124 560,64 970,50 L970,200 L0,200 Z" fill="url(#bandGlow)"/>
  </svg>

  <address class="postal-address">PO BOX 4829, Marlow Vale 3891</address>

  <ul class="contact-list">
    <li class="contact-list__item contact-list__item--phone">
      <svg class="contact-list__icon" viewBox="0 0 14 14"><path d="M4 0h6a1 1 0 0 1 1 1v12a1 1 0 0 1-1 1H4a1 1 0 0 1-1-1V1a1 1 0 0 1 1-1zm0 2v9h6V2z"/></svg>
      03 5461 8237
    </li>
    <li class="contact-list__item">
      <svg class="contact-list__icon" viewBox="0 0 14 14"><path d="M4 0h6v4H4zM1 5h12a1 1 0 0 1 1 1v6a1 1 0 0 1-1 1H1a1 1 0 0 1-1-1V6a1 1 0 0 1 1-1z"/></svg>
      03 5387 9216
    </li>
    <li class="contact-list__item">
      <svg class="contact-list__icon" viewBox="0 0 14 14"><path d="M1 2h12a1 1 0 0 1 1 1v8a1 1 0 0 1-1 1H1a1 1 0 0 1-1-1V3a1 1 0 0 1 1-1zm0 1.5V4l6 4 6-4v-.5z"/></svg>
      sales@brindarockets.com.au
    </li>
    <li class="contact-list__item">
      <svg class="contact-list__icon" viewBox="0 0 14 14"><path d="M7 0a7 7 0 1 1 0 14A7 7 0 0 1 7 0zm0 1.3C6 2.6 5.4 4.6 5.3 6.3h3.4C8.6 4.6 8 2.6 7 1.3zM1.4 7.7a5.7 5.7 0 0 0 3.3 4.6A9 9 0 0 1 4 7.7zm8.6 0a9 9 0 0 1-.7 4.6 5.7 5.7 0 0 0 3.3-4.6zM5.3 7.7c.1 1.7.7 3.7 1.7 5 1-1.3 1.6-3.3 1.7-5zM4.7 1.7a5.7 5.7 0 0 0-3.3 4.6H4a9 9 0 0 1 .7-4.6zm4.6 0a9 9 0 0 1 .7 4.6h2.6a5.7 5.7 0 0 0-3.3-4.6z"/></svg>
      www.brindarockets.com.au
    </li>
  </ul>
</main>
</body>
</html>
```